Funky Modern Flyer A5 or Postcard size

Hi, I am looking at a one small flyer (A5 or postcard size) that I can put both on my website on the front page (ie so png) and also send out if necessary.

It has to be modern, funky and hip. My brand is professional / Corporate so it also has to fit in with that brand.

There are 6 attachments:
Example 1 - FernaPeak - I like this look, clean, modern, funky and says it all.
Example 2 - FernPeak - again another look I like, simple, explanatory
Example 4 - Brightstall Bazaar - font is cool on this one but background not so much too much going on but I like the font
Example 5 - Example 4 - Brightstall Bazaar - font is cool on this one but background not so much too much going on but I like the font
5 is my logo
Example 6 is something I found on the web this morning which is effective.

It is for a Mentoring and Training program I run called: HIGHSTRIDE

What is to be included is the following:
The name: Highstride
Somewhere: Training, Mentoring
My Logo (see attached two options) you can choose which colour suits and I have the source file should you need it
My website and email: www.miriambaskell.example / miriam@miriambaskell.example

This wording: This is one of our highest in-demand programs and is based on a background and proven track record by Miriam in accelerating sales organisations and their people into stand out high performers. **(NOTE this wording in this paragraph may change and I am open to you changing if you think you can make it more effective!)

Colours: white, black and gold (those are our website colours).

I'd like the Highstride to really stand out.... I have included two fonts that I really like that I got off Brightstall Bazaar. However, feel free to suggest other fonts that you think cool or funky!
Updates

Hi everyone, just to add a note to the brief, I am not overly keen on pictures that are really busy. I only like a picture that is minimal and effective. The examples from Brightstall Bazaar was more for the Font Style not so much the pictures in the background. The pictures can take away from a design unless done really minimally.....hope this makes sense. Miriam Added Wednesday, March 15, 2017

Target Market(s)

My target Market is Corporates but I want a Funky Modern look as a lot of people in Corporates are Millennials as well which is part of my target market

Industry/Entity Type

Information Technology

Requirements
Must have
• What is to be included is the following:
• The name: Highstride
• Somewhere: Training, Mentoring
• My Logo (see attached two options) you can choose which colour suits and I have the source file should you need it
• My website and email: www.miriambaskell.example / miriam@miriambaskell.example
• This wording: This is one of our highest in-demand programs and is based on a background and proven track record in high performance and accelerating sales organisations and their people into stand out high performers. (**NOTE this wording may change when final design is picked to be changed as still working in it***)
• Colours: white, black and gold (those are our website colours).
• I'd like the Highstride to really stand out.... I have included two fonts that I really like that I got off Brightstall Bazaar. However, feel free to suggest other fonts that you think cool or funky! NOTE: The pictures I have attached is mainly for the FONTS not for the background pictures. I am not that keen on background pictures as it can take away from the font - unless it is minimal
Should not have
• Too many different colours, I like slick, modern, clean. White, gold and black preferred as this is our website colour.
• NOTE: The pictures from Brightstall Bazaar I have attached are mainly for the FONTS not for the background pictures. I am not hugely keen on background pictures as it can take away from the font/message - unless the pictures are minimal but effective.

```html
<!DOCTYPE html>
<html lang="en">
<head>
<meta charset="utf-8">
<title>Miriam Baskell – Highstride Flyer</title>
<link href="https://fonts.googleapis.com/css2?family=Roboto+Condensed:wght@700&family=Raleway:wght@400&family=Lato:wght@400&family=Kaushan+Script&display=swap" rel="stylesheet">
<style>
  :root {
    --gold: #e3b532;
    --gold-light: #f0df96;
    --gold-deep: #c9982a;
    --ink: #232323;
    --paper: #ffffff;
    --photo-light: #e2e2e2;
    --photo-dark: #5a5a5a;
  }
  html, body {
    margin: 0;
    padding: 0;
    width: 1200px;
    height: 1200px;
    overflow: hidden;
    background: var(--paper);
  }
  .flyer {
    position: absolute;
    left: 240px;
    top: 46px;
    width: 770px;
    height: 1082px;
    background: var(--paper);
    overflow: hidden;
  }
  .flyer-shapes {
    position: absolute;
    inset: 0;
    width: 100%;
    height: 100%;
  }
  .brand-mark {
    position: absolute;
    left: 362px;
    top: 58px;
    width: 46px;
    height: 46px;
    border-radius: 50%;
    background: var(--gold);
  }
  .brand-name {
    position: absolute;
    left: 0;
    width: 100%;
    top: 152px;
    text-align: center;
    font-family: "Raleway", sans-serif;
    font-weight: 400;
    font-size: 30px;
    letter-spacing: 1px;
    color: var(--gold);
    margin: 0;
  }
  .headline {
    position: absolute;
    left: 0;
    width: 100%;
    text-align: center;
    font-family: "Roboto Condensed", sans-serif;
    font-weight: 700;
    font-size: 58px;
    line-height: 1;
    margin: 0;
  }
  .headline-top { top: 306px; color: var(--gold); }
  .headline-bottom { top: 368px; color: var(--ink); }
  .region {
    position: absolute;
    top: 440px;
    left: 0;
    width: 100%;
    display: flex;
    align-items: center;
    justify-content: center;
    gap: 10px;
    font-family: "Raleway", sans-serif;
    font-size: 31px;
    color: var(--ink);
  }
  .region-rule {
    width: 161px;
    height: 7px;
    background: var(--gold-light);
  }
  .program-name {
    position: absolute;
    top: 494px;
    left: 0;
    width: 100%;
    text-align: center;
    font-family: "Kaushan Script", cursive;
    font-size: 96px;
    line-height: 1.2;
    color: var(--ink);
    margin: 0;
  }
  .program-summary {
    position: absolute;
    top: 636px;
    left: 82px;
    width: 640px;
    text-align: justify;
    text-align-last: center;
    font-family: "Lato", sans-serif;
    font-size: 16px;
    line-height: 21px;
    color: var(--ink);
    margin: 0;
  }
  .portrait {
    position: absolute;
    left: 0;
    top: 714px;
    width: 336px;
    height: 368px;
    background: linear-gradient(160deg, var(--photo-light) 0%, #a8a8a8 45%, var(--photo-dark) 100%);
    clip-path: polygon(0 0, 262px 0, 262px 170px, 336px 215px, 336px 100%, 0 100%);
  }
  .call-now {
    position: absolute;
    top: 824px;
    left: 278px;
    font-family: "Roboto Condensed", sans-serif;
    font-weight: 700;
    font-size: 47px;
    line-height: 1;
    margin: 0;
    white-space: nowrap;
  }
  .call-now .label { color: var(--gold); }
  .call-now .number { color: var(--ink); }
  .contact-list {
    position: absolute;
    left: 374px;
    top: 918px;
    margin: 0;
    padding: 0;
    list-style: none;
    font-family: "Lato", sans-serif;
    font-size: 22px;
    color: var(--ink);
  }
  .contact-list li {
    display: flex;
    align-items: center;
    gap: 10px;
    height: 47px;
  }
  .contact-icon { width: 18px; height: 18px; flex: none; }
</style>
</head>
<body>
  <div class="flyer">
    <svg class="flyer-shapes" viewBox="0 0 962 1352" preserveAspectRatio="none" aria-hidden="true">
      <defs>
        <linearGradient id="goldSheen" x1="0" y1="0" x2="1" y2="0">
          <stop offset="0" stop-color="#f0df96"/>
          <stop offset="0.3" stop-color="#d9b453"/>
          <stop offset="0.55" stop-color="#c9982a"/>
          <stop offset="0.8" stop-color="#f0df96"/>
          <stop offset="1" stop-color="#d4a73c"/>
        </linearGradient>
      </defs>
      <polygon class="header-gold" fill="url(#goldSheen)" points="0,0 962,0 962,247 840,180 497,356 125,180 0,247"/>
      <polygon class="header-dark" fill="#232323" points="370,0 600,0 835,176 497,342 130,176"/>
      <rect class="footer-band" x="0" y="1287" width="962" height="65" fill="#232323"/>
    </svg>

    <div class="brand-mark" aria-hidden="true"></div>
    <p class="brand-name">MIRIAM BASKELL</p>

    <h1 class="headline headline-top">EXECUTIVE DIGITAL</h1>
    <h2 class="headline headline-bottom">SALES STRATEGIST</h2>

    <div class="region">
      <span class="region-rule"></span>
      <span>Australia &amp; NZ</span>
      <span class="region-rule"></span>
    </div>

    <p class="program-name">Highstride</p>

    <p class="program-summary">This is one of our highest in-demand programs and is based on a background and proventrackrecord in high performanceand accelerating ' 1 sales organisations and their peopleinto stand out high performers</p>

    <div class="portrait" role="img" aria-label="Black and white portrait photo of Miriam in a floral blouse"></div>

    <p class="call-now"><span class="label">CALL NOW</span> <span class="number">6420557193</span></p>

    <ul class="contact-list">
      <li>
        <svg class="contact-icon" viewBox="0 0 20 20" aria-hidden="true">
          <circle cx="10" cy="10" r="8.5" fill="none" stroke="#e3b532" stroke-width="2"/>
          <ellipse cx="10" cy="10" rx="3.5" ry="8.5" fill="none" stroke="#e3b532" stroke-width="1.5"/>
          <line x1="1.5" y1="10" x2="18.5" y2="10" stroke="#e3b532" stroke-width="1.5"/>
        </svg>
        <span>www.miriambaskell.example</span>
      </li>
      <li>
        <svg class="contact-icon" viewBox="0 0 20 20" aria-hidden="true">
          <rect x="1" y="4" width="18" height="13" fill="#e3b532"/>
          <polyline points="1,4 10,11 19,4" fill="none" stroke="#ffffff" stroke-width="1.5"/>
        </svg>
        <span>miriam@miriambaskell.example</span>
      </li>
    </ul>
  </div>
</body>
</html>
```